Signage setout with photos for side of Mowing Trailer

We need signage for our mowing trailer to attract new business.
Specifically a Rear sign 1470x880mm and Side signs 2400x880mm
Sign needs to be modern and professional.
Some example uploads as to what we have thought about so far.
Logo doesn't need to be the green colour.
Logo words and Logo of Mower do not need to be together.
Link to get a mower image>
https://brightfieldgear.example/tandem
Updates

Need extra days to review

Target Market(s)

Other Customers driving past the trailer.

Industry/Entity Type

Lawnmowing / Landscaping

Requirements
Must have
• Phone Number, Company Name & Logo, Web address, Chatterlane and Pixo Logos, Comment - "Acreage & Commercial Specialists" Catchcry - "100% Electric Mowing Company - est 2017" Services "Mowing, Hedging, Pressure Cleaning, Weed Control, Fencing, Turfing, Mulching and Rubbish Removal"
Nice to have
• Full colour background images.

```html
<!DOCTYPE html>
<html lang="en">
<head>
<meta charset="utf-8">
<title>Fresh Field Mowing – Trailer Signage</title>
<link href="https://fonts.googleapis.com/css2?family=Open+Sans:wght@600;700&family=Arimo:wght@700&display=swap" rel="stylesheet">
<style>
  :root{
    --ink:#2c6a33;
    --ink-dark:#24582a;
    --halo:#ffffff;
    --lawn-light:#a9d957;
    --lawn:#6fb52c;
    --lawn-deep:#4f9a1f;
    --bloom:#d9418f;
    --veil:rgba(255,255,255,0.42);
    --badge:#e8692a;
    --page:#ffffff;
  }
  *{margin:0;padding:0;box-sizing:border-box}
  html,body{width:1200px;height:900px;overflow:hidden;background:var(--page)}
  body{position:relative;font-family:"Open Sans",Arial,sans-serif;color:var(--ink)}
  .sign{position:absolute;left:161px;overflow:hidden}
  .sign--rear{top:97px;width:540px;height:323px}
  .sign--side{top:486px;width:882px;height:323px}
  .sign__photo{position:absolute;inset:0;
    background:
      radial-gradient(ellipse 45% 30% at 85% 8%, var(--bloom) 0%, rgba(217,65,143,0) 70%),
      linear-gradient(180deg,#5f9a3a 0%,var(--lawn-light) 28%,var(--lawn) 60%,var(--lawn-deep) 100%);}
  .sign--rear .sign__photo::after{content:"";position:absolute;left:200px;top:20px;width:200px;height:300px;
    background:radial-gradient(ellipse at 50% 60%,rgba(60,190,40,0.55),rgba(60,190,40,0) 70%)}
  .txt{position:absolute;white-space:nowrap;text-align:center;
    text-shadow:0 0 2px var(--halo),0 0 2px var(--halo),0 0 3px var(--halo),0 0 3px var(--halo)}
  .veil{position:absolute;background:var(--veil)}
  .veil--round{border-radius:50%}
  .brand{position:absolute;text-align:center;font-weight:700;color:var(--ink)}
  .brand__dot{display:block;margin:0 auto 6px;border-radius:50%;background:var(--badge)}
  .brand__name{display:block;line-height:1.02;letter-spacing:0.5px}
  .brand__est{display:block;font-weight:600}
  .phone{position:absolute;display:flex;align-items:center;font-weight:700;white-space:nowrap}
  .phone svg{flex:none}
  .social{position:absolute;display:flex;align-items:center;gap:10px;font-weight:700;white-space:nowrap}
  .social__item{display:flex;align-items:center;gap:4px}
  .social__mark{display:inline-block;background:var(--ink);border-radius:3px}
  .services{font-family:"Arimo",Arial,sans-serif;font-weight:700;line-height:1.22}
  .web{font-family:"Arimo",Arial,sans-serif;font-weight:700}
</style>
</head>
<body>

<!-- Rear sign 1470 x 880 -->
<section class="sign sign--rear">
  <div class="sign__photo" role="img" aria-label="Garden lawn with flower beds and an operator riding an electric zero-turn mower"></div>
  <div class="veil veil--round" style="left:-12px;top:-15px;width:218px;height:218px"></div>
  <div class="veil" style="left:220px;top:4px;width:320px;height:73px"></div>
  <div class="veil" style="left:0;top:257px;width:540px;height:50px"></div>

  <div class="brand" style="left:8px;top:40px;width:180px">
    <span class="brand__dot" style="width:38px;height:38px"></span>
    <span class="brand__name" style="font-size:20px">FRESH FIELD<br><span style="font-size:26px">MOWING</span></span>
    <span class="brand__est" style="font-size:16px;margin-top:2px">– est 2017 –</span>
  </div>

  <div class="txt" style="left:220px;top:8px;width:320px;font-size:27px;font-weight:600;line-height:1.3">Acreage &amp; Commercial<br>Specialists</div>

  <div class="phone" style="left:318px;top:90px;font-size:33px;gap:8px">
    <svg width="28" height="28" viewBox="0 0 28 28" aria-hidden="true"><rect width="28" height="28" rx="6" fill="#2c6a33"/><path d="M9 6c1-.6 2-.4 2.6.5l1.6 2.8c.4.8.2 1.6-.5 2.1l-1.3 1c.8 1.8 2.2 3.3 4 4.2l1-1.3c.5-.7 1.4-.9 2.1-.5l2.8 1.6c.9.5 1.1 1.6.5 2.5-.9 1.4-2.4 2.3-4.1 1.8C12 19.400 8.400 15.700 7.300 10.300c-.3-1.700.4-3.500 1.700-4.300z" fill="#fff"/></svg>
    <span class="txt" style="position:static">3900 4127</span>
  </div>
  <div class="txt web" style="left:310px;top:131px;width:222px;font-size:11.5px">www.freshfieldmowing.example</div>
  <div class="social" style="left:380px;top:151px;font-size:13px">
    <span class="social__item"><span class="social__mark" style="width:12px;height:12px"></span><span class="txt" style="position:static">Chatterlane</span></span>
    <span class="social__item"><span class="social__mark" style="width:12px;height:12px"></span><span class="txt" style="position:static">Pixo</span></span>
  </div>

  <div class="txt" style="left:10px;top:200px;width:520px;font-size:33px;font-weight:700;letter-spacing:-0.3px">100%&nbsp; Electric Mowing Company</div>

  <div class="txt services" style="left:0;top:258px;width:540px;font-size:18px">Mowing • Hedging • Pressure Cleaning • Weed Control<br>Fencing • Turfing • Mulching • Rubbish Removal</div>
</section>

<!-- Side sign 2400 x 880 -->
<section class="sign sign--side">
  <div class="sign__photo" role="img" aria-label="Manicured garden lawn with pink flower beds and shrubs"></div>
  <div class="veil veil--round" style="left:0;top:-4px;width:268px;height:268px"></div>
  <div class="veil" style="left:0;top:20px;width:882px;height:28px"></div>
  <div class="veil" style="left:150px;top:256px;width:732px;height:55px"></div>

  <div class="brand" style="left:30px;top:40px;width:210px">
    <span class="brand__dot" style="width:62px;height:62px;margin-bottom:12px"></span>
    <span class="brand__name" style="font-size:26px">FRESH FIELD<br><span style="font-size:33px">MOWING</span></span>
    <span class="brand__est" style="font-size:22px;margin-top:2px">– est 2017 –</span>
  </div>

  <div class="txt" style="left:250px;top:12px;width:600px;font-size:34px;font-weight:600">Acreage &amp; Commercial Specialists</div>

  <div class="phone" style="left:304px;top:80px;font-size:55px;gap:18px">
    <svg width="54" height="54" viewBox="0 0 28 28" aria-hidden="true"><rect width="28" height="28" rx="6" fill="#2c6a33" stroke="#fff" stroke-width="1"/><path d="M9 6c1-.6 2-.4 2.6.5l1.6 2.8c.4.8.2 1.6-.5 2.1l-1.3 1c.8 1.8 2.2 3.3 4 4.2l1-1.3c.5-.7 1.4-.9 2.1-.5l2.8 1.6c.9.5 1.1 1.6.5 2.5-.9 1.4-2.4 2.3-4.1 1.8C12 19.400 8.400 15.700 7.300 10.300c-.3-1.700.4-3.500 1.700-4.300z" fill="#fff"/></svg>
    <span class="txt" style="position:static">3900 4127</span>
  </div>
  <div class="social" style="left:686px;top:96px;font-size:17px;flex-direction:column;align-items:flex-start;gap:4px">
    <span class="social__item"><span class="social__mark" style="width:16px;height:16px"></span><span class="txt" style="position:static">Chatterlane</span></span>
    <span class="social__item"><span class="social__mark" style="width:16px;height:16px"></span><span class="txt" style="position:static">Pixo</span></span>
  </div>

  <div class="txt web" style="left:250px;top:144px;width:520px;font-size:26px">www.freshfieldmowing.example</div>

  <div class="txt" style="left:240px;top:188px;width:630px;font-size:40px;font-weight:700;letter-spacing:-0.3px">100% Electric Mowing Company</div>

  <div class="txt services" style="left:240px;top:256px;width:630px;font-size:21.5px">Mowing • Hedging • Pressure Cleaning • Weed Control<br>Fencing • Turfing • Mulching • Rubbish Removal</div>
</section>

</body>
</html>
```